Brambury Logistics

Create a modern, simple, Elegant business card design for my business.

Services: Tamo Trucks, Transport, Contract Logistics,

Industry/Entity Type

Business

Contact Information for Business Card

Include all details same as old card plus new website address: www.bramburylogistics.com.au

Requirements
Must have
• Similar colors to Logo.

```html
<!DOCTYPE html>
<html lang="en">
<head>
<meta charset="utf-8">
<title>Brambury Logistics – Business Card</title>
<link href="https://fonts.googleapis.com/css2?family=Open+Sans:wght@700&family=Questrial&display=swap" rel="stylesheet">
<style>
  :root {
    --backdrop: #dedad7;
    --card-grey: #cfd0d2;
    --card-grey-light: #d6d7d9;
    --blue-deep: #0f4a76;
    --blue-bright: #0774ad;
    --shadow: #3a3a3a;
    --white: #ffffff;
    --title-tint: #c9d9e7;
    --brand-grey: #8d8f92;
  }
  html, body {
    margin: 0;
    width: 1200px;
    height: 1000px;
    overflow: hidden;
    background: var(--backdrop);
  }
  .canvas { position: relative; width: 1200px; height: 1000px; }
  .card {
    position: absolute;
    width: 677px;
    height: 411px;
    background: var(--card-grey);
    box-shadow: 8px 8px 4px var(--shadow);
    overflow: hidden;
  }
  .card svg.card-art { position: absolute; inset: 0; }
  .card--front { left: 44px; top: 73px; }
  .card--back { left: 477px; top: 547px; height: 413px; }

  .contact {
    position: absolute;
    right: 58px;
    top: 62px;
    text-align: right;
    color: var(--white);
    font-family: "Questrial", sans-serif;
  }
  .contact__name {
    margin: 0;
    font-family: "Open Sans", sans-serif;
    font-weight: 700;
    font-size: 18px;
    letter-spacing: 0.5px;
  }
  .contact__title {
    margin: 14px 0 0;
    font-size: 17px;
    color: var(--title-tint);
  }
  .contact__list {
    list-style: none;
    margin: 52px 0 0;
    padding: 0;
    font-size: 19px;
    line-height: 43px;
    letter-spacing: 0.3px;
  }
  .brand {
    position: absolute;
    font-family: "Questrial", sans-serif;
    color: var(--brand-grey);
    white-space: nowrap;
  }
  .card--front .brand { left: 22px; top: 318px; font-size: 30px; }
  .card--back .brand { left: 70px; top: 150px; font-size: 56px; }
</style>
</head>
<body>
<main class="canvas">
  <section class="card card--front" aria-label="Business card front">
    <svg class="card-art" width="677" height="411" viewBox="0 0 677 411" aria-hidden="true">
      <defs>
        <linearGradient id="frontBlue" x1="0" y1="0" x2="1" y2="0">
          <stop offset="0" stop-color="var(--blue-deep)"/>
          <stop offset="1" stop-color="var(--blue-bright)"/>
        </linearGradient>
      </defs>
      <polygon points="261,0 677,0 677,343 210,411 0,411 0,267" fill="url(#frontBlue)"/>
    </svg>
    <div class="contact">
      <h1 class="contact__name">JODY MARSH</h1>
      <p class="contact__title">Regional Manager</p>
      <ul class="contact__list">
        <li>w. www.bramburylogistics.com.au</li>
        <li>e. jodymarsh@bramburylogistics.com.au</li>
        <li>m. 0412305689</li>
      </ul>
    </div>
    <div class="brand">Brambury Logistics</div>
  </section>

  <section class="card card--back" aria-label="Business card back">
    <svg class="card-art" width="677" height="413" viewBox="0 0 677 413" aria-hidden="true">
      <defs>
        <linearGradient id="backGrey" x1="0" y1="0" x2="0" y2="1">
          <stop offset="0" stop-color="var(--card-grey-light)"/>
          <stop offset="1" stop-color="var(--card-grey)"/>
        </linearGradient>
        <linearGradient id="backBlue" x1="0" y1="0" x2="1" y2="0">
          <stop offset="0" stop-color="var(--blue-deep)"/>
          <stop offset="1" stop-color="var(--blue-bright)"/>
        </linearGradient>
      </defs>
      <rect width="677" height="413" fill="url(#backGrey)"/>
      <polygon points="0,286 677,178 677,413 0,413" fill="url(#backBlue)"/>
    </svg>
    <div class="brand">Brambury Logistics</div>
  </section>
</main>
</body>
</html>
```